Ned Halvorsen Executive Coach Business Card Design

I need a new card design for my Executive Coaching practice. I am a Clinical Psychotherapist and Executive Coach. I help my clients get the most out of life by developing their personal and professional skills and abilities.

I work with senior executives. My design needs to be high end. I am thinking gloss on the front. I am also thinking contemporary. I am going to use a black, grey and red colour scheme on the the website. I am thinking grey with black and red accents. I would also like a water mark included on the card.

Target Market(s)

Senior Executives In major Companies

Industry/Entity Type

Business

Contact Information for Business Card

On the front

Ned Halvorsen
Clinical Psychotherapist and Executive Coach
For Personal and Professional Success

On the Back

Tarwin office
87 Tarwin Vale Road Tarwin

North Sydney Office
Suite 309 / 41 Lathom Street North Sydney

Pellington Street Office
Suite 512 / 218 Pellington Street Sydney CBD

Phone 02 95817364
Email ned@nedhalvorsen.com.au

Requirements
Must have
• Friendly but professional
Water Mark
Gloss Front

```html
<!DOCTYPE html>
<html lang="en">
<head>
<meta charset="utf-8">
<title>Ned Halvorsen – Business Card</title>
<link rel="stylesheet" href="https://fonts.googleapis.com/css2?family=Bitter:wght@400;700&family=Open+Sans:wght@400;600&display=swap">
<style>
  :root {
    --stage: #e6e4e1;
    --card-red: #f50000;
    --watermark-red: #ff3a3a;
    --ink-white: #ffffff;
    --ink-dark: #1f1f1f;
    --band-black: #050505;
    --accent-red: #e60000;
    --shadow: rgba(0, 0, 0, 0.28);
  }
  * { margin: 0; padding: 0; box-sizing: border-box; }
  html, body {
    width: 1200px; height: 492px; overflow: hidden;
    background: var(--stage);
  }
  .stage {
    position: relative; width: 1200px; height: 492px;
  }
  .card {
    position: absolute;
    box-shadow: 0 6px 18px var(--shadow);
    overflow: hidden;
  }

  /* Front */
  .card-front {
    left: 40px; top: 86px; width: 520px; height: 320px;
    background: var(--card-red);
    color: var(--ink-white);
    font-family: "Bitter", Georgia, serif;
    text-align: center;
  }
  .card-front .name {
    position: absolute; left: 0; right: 0; top: 52px;
    font-size: 46px; font-weight: 400; letter-spacing: 0.5px;
  }
  .card-front .watermark {
    position: absolute; left: 0; right: 0; top: 134px;
    font-size: 46px; font-weight: 400; color: var(--watermark-red);
  }
  .card-front .tagline {
    position: absolute; left: 0; right: 0; top: 222px;
    font-size: 20px; line-height: 1.25;
  }

  /* Back */
  .card-back {
    left: 610px; top: 80px; width: 550px; height: 332px;
    background: var(--ink-white);
    font-family: "Open Sans", Arial, sans-serif;
    text-align: center;
  }
  .card-back .name {
    position: absolute; left: 0; right: 0; top: 70px;
    font-family: "Bitter", Georgia, serif;
    font-weight: 700; font-size: 28px; color: var(--accent-red);
  }
  .contact {
    position: absolute; left: 0; right: 0; top: 150px;
    font-size: 16px; color: var(--ink-dark); line-height: 26px;
  }
  .contact svg { width: 13px; height: 13px; vertical-align: -1px; margin-right: 4px; }
  .curve-band { position: absolute; left: 0; bottom: 0; width: 550px; height: 130px; }
  .offices {
    position: absolute; left: 0; right: 0; bottom: 14px;
    list-style: none; color: var(--ink-white); font-size: 14px; line-height: 27px;
  }
  .offices li:nth-child(1) { padding-left: 60px; }
  .offices li:nth-child(2) { padding-left: 20px; }
  .offices svg { width: 11px; height: 14px; vertical-align: -2px; margin-right: 8px; }
</style>
</head>
<body>
<main class="stage">

  <section class="card card-front" aria-label="Card front">
    <h1 class="name">Ned Halvorsen</h1>
    <p class="watermark" aria-hidden="true">Ned Halvorsen</p>
    <p class="tagline">Clinical Psychotherapist and Executive Coach<br>For Personal and Professional Success</p>
  </section>

  <section class="card card-back" aria-label="Card back">
    <h2 class="name">Ned Halvorsen</h2>
    <div class="contact">
      <p>
        <svg viewBox="0 0 24 24" aria-hidden="true"><circle cx="12" cy="12" r="10.5" fill="none" stroke="#1f1f1f" stroke-width="2"/><path d="M8 6.5c-1 1-1 3.5 1.5 6.5s5 4 6.5 3l1-1.5-2.5-2-1.3 1c-1-.5-2.5-2-3-3l1-1.3-2-2.5z" fill="#1f1f1f"/></svg>02 95817364
      </p>
      <p>
        <svg viewBox="0 0 24 24" aria-hidden="true"><path d="M2 9l10-6 10 6v11H2z" fill="#1f1f1f"/><path d="M3 9l9 6 9-6" fill="none" stroke="#fff" stroke-width="1.6"/></svg>ned@nedhalvorsen.com.au
      </p>
    </div>

    <svg class="curve-band" viewBox="0 0 550 130" preserveAspectRatio="none" aria-hidden="true">
      <path d="M0 130 C 60 40, 250 0, 550 18 L 550 130 Z" fill="var(--accent-red)"/>
      <path d="M0 130 C 70 52, 260 14, 550 30 L 550 130 Z" fill="var(--band-black)"/>
    </svg>

    <ul class="offices">
      <li><svg viewBox="0 0 12 16" aria-hidden="true"><path d="M6 0a6 6 0 0 0-6 6c0 4.5 6 10 6 10s6-5.5 6-10a6 6 0 0 0-6-6zm0 8.5A2.5 2.5 0 1 1 6 3.5a2.5 2.5 0 0 1 0 5z" fill="#fff"/></svg>87 Tarwin Vale Road Tarwin North Sydney</li>
      <li><svg viewBox="0 0 12 16" aria-hidden="true"><path d="M6 0a6 6 0 0 0-6 6c0 4.5 6 10 6 10s6-5.5 6-10a6 6 0 0 0-6-6zm0 8.5A2.5 2.5 0 1 1 6 3.5a2.5 2.5 0 0 1 0 5z" fill="#fff"/></svg>Suite 512 / 218 Pellington Street Sydney CBD</li>
      <li><svg viewBox="0 0 12 16" aria-hidden="true"><path d="M6 0a6 6 0 0 0-6 6c0 4.5 6 10 6 10s6-5.5 6-10a6 6 0 0 0-6-6zm0 8.5A2.5 2.5 0 1 1 6 3.5a2.5 2.5 0 0 1 0 5z" fill="#fff"/></svg>Suite 309 / 41 Lathom Street North Sydney Pellington Street</li>
    </ul>
  </section>

</main>
</body>
</html>
```